PawHush business card

Looking for a fun and cool biz card for a new company with patent pending products. I have products to help and protect dogs hearing. My colors are pantone blue and orange.
Updates

Please add tag line: Protect the ones you love...even your PawHushes!

Target Market(s)

Animal/Dog lovers!

Industry/Entity Type

Retail

Contact Information for Business Card

I'm looking for something simple yet fun with all the info included for biz cards

Colors
0555a3
f78f20

Requirements
Must have
• Logo
Nice to have
• name, website and email
Should not have
• phone number

```html
<!DOCTYPE html>
<html lang="en">
<head>
<meta charset="utf-8">
<title>PawHush business card</title>
<link rel="stylesheet" href="https://fonts.googleapis.com/css2?family=Roboto:wght@400;500;700&display=swap">
<style>
  :root {
    --brand-blue: #0555a3;
    --brand-blue-light: #1a6cbc;
    --brand-blue-deep: #03457f;
    --brand-orange: #f78f20;
    --paper: #ffffff;
    --stage: #e9e6e1;
    --text-light: #ffffff;
    --text-muted: #d6e6f7;
  }
  * { box-sizing: border-box; margin: 0; padding: 0; }
  html, body { width: 912px; height: 1200px; overflow: hidden; }
  body {
    background: var(--stage);
    font-family: "Roboto", Arial, sans-serif;
    display: flex;
    flex-direction: column;
    align-items: center;
    justify-content: center;
    gap: 50px;
  }
  .card {
    position: relative;
    width: 560px;
    height: 320px;
    border-radius: 16px;
    overflow: hidden;
    box-shadow: 0 6px 18px rgba(0,0,0,0.18);
  }
  .card--blue {
    background: linear-gradient(135deg, var(--brand-blue-light) 0%, var(--brand-blue) 50%, var(--brand-blue-deep) 100%);
    color: var(--text-light);
  }
  .card--white { background: var(--paper); }

  .brand {
    display: flex;
    align-items: center;
    gap: 10px;
    color: var(--brand-orange);
    font-weight: 700;
    letter-spacing: -0.5px;
    white-space: nowrap;
  }
  .brand__dot { border-radius: 50%; background: var(--brand-orange); flex: none; }

  /* Front: contact details */
  .front .brand { position: absolute; left: 40px; top: 40px; font-size: 54px; line-height: 1; }
  .front .brand__dot { width: 22px; height: 22px; }
  .person { position: absolute; left: 44px; top: 130px; }
  .person__name { font-size: 20px; font-weight: 500; letter-spacing: 0.5px; }
  .person__role { font-size: 13px; color: var(--text-muted); margin-top: 2px; }
  .address { margin-top: 14px; font-size: 14px; line-height: 1.4; }
  .contacts { list-style: none; margin-top: 10px; font-size: 14px; line-height: 1.6; }
  .contacts li { display: flex; align-items: center; gap: 10px; }
  .contacts svg { width: 12px; height: 12px; fill: var(--text-light); flex: none; }

  /* Back: large brand */
  .feature { display: flex; align-items: center; justify-content: center; }
  .feature .brand { font-size: 76px; color: var(--brand-orange); }
  .feature .brand__dot { width: 30px; height: 30px; }

  /* Back: logo, tagline and web */
  .logo-side { display: flex; flex-direction: column; align-items: center; justify-content: center; gap: 14px; }
  .logo-side .brand { font-size: 66px; line-height: 1; }
  .logo-side .brand__dot { width: 26px; height: 26px; }
  .tagline { font-size: 16px; font-style: italic; color: var(--text-muted); }
  .web { font-size: 17px; letter-spacing: 0.4px; margin-top: 10px; }
</style>
</head>
<body>

  <section class="card card--blue front" aria-label="Card front with contact details">
    <div class="brand"><span class="brand__dot"></span><span class="brand__name">PawHush</span></div>
    <div class="person">
      <p class="person__name">DANIEL REYES</p>
      <p class="person__role">Director</p>
      <p class="address">118 Alder Lane, Suite 5<br>Portland OR 97201</p>
      <ul class="contacts">
        <li><svg viewBox="0 0 12 12"><path d="M0 2h12v8H0z M1 3l5 3.5L11 3v-.2H1z" fill-rule="evenodd"/></svg>info@pawhush.com</li>
        <li><svg viewBox="0 0 12 12"><circle cx="6" cy="6" r="5.5"/></svg>www.pawhush.com</li>
      </ul>
    </div>
  </section>

  <section class="card card--white feature" aria-label="Card back with brand name">
    <div class="brand"><span class="brand__dot"></span><span class="brand__name">PawHush</span></div>
  </section>

  <section class="card card--blue logo-side" aria-label="Card back with name, tagline and website">
    <div class="brand"><span class="brand__dot"></span><span class="brand__name">PawHush</span></div>
    <p class="tagline">Protect the ones you love...even your PawHushes!</p>
    <p class="web">www.pawhush.com</p>
  </section>

</body>
</html>
```